Profesional personal website needs design and business card

I need a business card with my professional name as a logo "Marlo Vitality" for my business. I am a Wellness Coach, consultant and trainer. So it should be professional, wellness oriented and modern.

Target Market(s)

Private clients, governments, corporations. Luxury and high market.

Industry/Entity Type

Health And Wellness

Contact Information for Business Card

Marlo Vitality should be the logo

Colors

Designer to choose colors to be used in the design.

Requirements
Must have
• Marlo Vitality
• Name: Tomás Arribal
• Wellness Coach, Consultant & Trainer.
• Website: www.marlovitality.example
• Phone:
• Spain (+34) 612 480 397
• (USA) +1 (555) 318 2046
Nice to have
• The most important is the design of "Marlo Vitality", as this is going to be my personal brand logo. It should be professional, wellness, high end and actual.
Should not have
• no golds, no baroque style..

```html
<!DOCTYPE html>
<html lang="en">
<head>
<meta charset="utf-8">
<title>Marlo Vitality — Business Card</title>
<link href="https://fonts.googleapis.com/css2?family=Barlow:wght@400;700&family=Parisienne&display=swap" rel="stylesheet">
<style>
  :root {
    --page: #e4e0d8;
    --card: #323643;
    --brand: #21b8c9;
    --ink-light: #b9cde0;
    --ink-white: #ffffff;
  }
  html, body {
    margin: 0;
    padding: 0;
    width: 1200px;
    height: 1200px;
    overflow: hidden;
    background: var(--page);
  }
  .card {
    position: absolute;
    left: 175px;
    width: 850px;
    height: 472px;
    background: var(--card);
    font-family: "Barlow", sans-serif;
    color: var(--ink-light);
  }
  .card--front { top: 88px; }
  .card--back { top: 640px; }

  .brand-mark {
    position: absolute;
    height: 430px;
    writing-mode: vertical-rl;
    font-family: "Barlow", sans-serif;
    font-weight: 700;
    font-size: 58px;
    line-height: 56px;
    text-align: center;
    letter-spacing: 1px;
    color: var(--brand);
    white-space: nowrap;
  }
  .card--front .brand-mark {
    left: 67px;
    top: 21px;
    transform: rotate(180deg);
  }
  .card--back .brand-mark {
    left: 735px;
    top: 20px;
  }

  .person-name {
    position: absolute;
    right: 75px;
    top: 78px;
    margin: 0;
    font-family: "Parisienne", cursive;
    font-weight: 400;
    font-size: 56px;
    line-height: 1;
    color: var(--ink-white);
  }
  .person-role {
    position: absolute;
    right: 95px;
    top: 146px;
    margin: 0;
    font-size: 18px;
    letter-spacing: 2.3px;
    color: var(--ink-light);
  }

  .contact-list {
    position: absolute;
    left: 421px;
    top: 370px;
    margin: 0;
    display: grid;
    grid-template-columns: 119px auto;
    row-gap: 2px;
    font-size: 21px;
    line-height: 24px;
    letter-spacing: 2px;
  }
  .contact-list dt, .contact-list dd { margin: 0; }

  .website {
    position: absolute;
    left: 131px;
    top: 214px;
    margin: 0;
    font-size: 28px;
    letter-spacing: 3.4px;
    color: var(--ink-light);
  }
</style>
</head>
<body>
  <section class="card card--front" aria-label="Business card front">
    <div class="brand-mark">Marlo Vitality</div>
    <h1 class="person-name">Tomás Arribal</h1>
    <p class="person-role">Wellness Coach, Consultant &amp; Trainer</p>
    <dl class="contact-list">
      <dt>Spain.</dt><dd>(+34) 612 480 397</dd>
      <dt>USA.</dt><dd>+1 (555) 318 2046</dd>
    </dl>
  </section>

  <section class="card card--back" aria-label="Business card back">
    <p class="website">www.marlovitality.example</p>
    <div class="brand-mark">Marlo Vitality</div>
  </section>
</body>
</html>
```